Stationary Set and Logo Update **PAYMENT GUARANTEED**

Stationery Design and Logo Update

About Us

Trindex Supply is a wholesale distributor of OEM [original brand] and compatible [generic brand] parts and supplies for use in copiers, faxes, printers, and multi-function machines. In plain English…we sell all the parts and supplies [such as toner] that make up any office equipment which outputs an image on paper.

Trindex was the 1st distributor to develop and sell a generic brand copier part in the United States. We have been in business since 1972 [nearly 40 years]. Our tagline is "The Steady Choice," as in our company was the first alternative product that copier dealers had to buying original brand copier parts. Trindex is known for offering reliable and cost-effective OEM and compatible products.

Project

We require a fresh, modern and corporate identity. Please submit a stationary package inclusive of a double-sided business card (2" x 3.5"), letterhead (8.5'x11"), and standard #10 envelope (4-1/8” x 9-1/2). You may use our current logo or preferably your take on an updated one. If an attempt is made in updating the logo #004D8E or a similar hue should be used as the primary color.

The design should be clean, simple, modern and professional and make an immediate impact.

Target Market(s)

Copier and printer dealers who lease and service imaging equipment in the United States and Latin America.

Industry/Entity Type

Business

Requirements
Must have
• Simple, clean, modern and professional. Please use #004D8E or a similar hue as the primary color. Letterhead must accommate (2) addresses. We have 2 locations.
Nice to have
• A simple, modern update to our current logo. https://assets.mailvorbo.example/fs030/5520384417702/img/418.jpg
Should not have
• More than (2) colors on logo.

```html
<!DOCTYPE html>
<html lang="en">
<head>
<meta charset="utf-8">
<title>Trindex Supply Stationery Set</title>
<link rel="stylesheet" href="https://fonts.googleapis.com/css2?family=Arimo:wght@400;700&display=swap">
<style>
:root{
  --brand:#0a4d96;
  --brand-deep:#0a2f66;
  --brand-soft:#1a5aa8;
  --brand-faint:#2a66b0;
  --paper:#ffffff;
  --backdrop:#efefef;
  --ink:#4a4a4a;
  --rule:#b9c8dc;
  --placeholder:#ececec;
}
*{margin:0;padding:0;box-sizing:border-box}
html,body{width:1200px;height:800px;overflow:hidden;background:var(--backdrop);font-family:"Arimo",Arial,sans-serif;color:var(--ink)}
.stage{position:relative;width:1200px;height:800px}
.piece{position:absolute;background:var(--paper);box-shadow:0 1px 3px rgba(0,0,0,.18)}

.wordmark{display:inline-flex;align-items:center;gap:.25em;font-weight:700;color:var(--brand);line-height:1;letter-spacing:-.01em;white-space:nowrap}
.wordmark .dot{width:.55em;height:.55em;border-radius:50%;background:var(--brand)}

/* Business card, contact side */
.card-back{left:28px;top:24px;width:332px;height:192px;display:flex}
.card-back .contact{width:114px;padding:12px 8px;font-size:5.6px;line-height:1.5;color:var(--brand)}
.card-back .wordmark{font-size:15px;margin-bottom:10px}
.card-back .contact p+p{margin-top:8px}
.card-back .field{flex:1;background:linear-gradient(90deg,var(--brand-deep),var(--brand) 60%,var(--brand-soft))}

/* Business card, name side */
.card-front{left:364px;top:24px;width:386px;height:192px;border-bottom:3px solid var(--brand)}
.card-front .band{height:36px;background:var(--brand);color:#fff;padding:7px 0 0 232px;font-size:8px;font-weight:700}
.card-front .band span{display:block;font-size:5.5px;font-weight:400;opacity:.8;margin-top:2px}
.card-front .wordmark{position:absolute;left:92px;top:82px;font-size:42px}

/* Presentation folder */
.folder{left:28px;top:224px;width:432px;height:572px;background:linear-gradient(90deg,var(--brand-deep),var(--brand) 55%,var(--brand-soft))}
.folder .wordmark{position:absolute;left:36px;top:262px;font-size:66px;color:var(--brand-faint)}
.folder .wordmark .dot{background:var(--brand-faint)}

/* Letterhead */
.letterhead{left:464px;top:224px;width:440px;height:572px;border-top:3px solid var(--brand);border-bottom:3px solid var(--brand);padding:42px 22px 0 44px;font-size:6.6px;line-height:1.9}
.sender{color:var(--brand);font-size:5.6px;line-height:1.4}
.recipient{margin-top:34px;line-height:1.6}
.subject{margin-top:14px;font-weight:700;letter-spacing:.06em}
.body-copy p{margin-top:14px}
.closing{margin-top:18px;margin-left:260px}
.signature{margin-left:268px;margin-top:4px;width:54px;height:16px;background:var(--placeholder)}
.letter-footer{position:absolute;left:44px;bottom:14px;font-size:5px;line-height:1.45;color:var(--brand)}
.letter-footer .wordmark{font-size:14px;margin-bottom:6px}
.letter-footer p+p{margin-top:6px}

/* Envelope */
.envelope{left:910px;top:120px;width:270px;height:676px;border-left:4px solid var(--brand)}
.envelope svg{position:absolute;left:0;top:0}
.envelope .return{position:absolute;left:104px;top:660px;transform:rotate(-90deg);transform-origin:left top;width:170px;font-size:5px;line-height:1.45;color:var(--brand);display:flex;gap:8px;align-items:flex-start}
.envelope .return .wordmark{font-size:16px;margin-top:8px}
</style>
</head>
<body>
<main class="stage">

  <section class="piece card-back" aria-label="Business card, contact side">
    <div class="contact">
      <div class="wordmark"><span class="dot"></span>Trindex</div>
      <p>Trindex Supply<br>Corporate Office<br>1820 Harbor Crest Drive<br>Palmera, FL 33400<br>Toll Free: 800-555-0162<br>Direct: 954-555-0148<br>Email: orders@trindexsupply.com</p>
      <p>Trindex West<br>West Coast Fulfillment Center<br>Ridgeline Commerce Park, Unit 4<br>75 Quarry Lane<br>Silvercreek, NV 89600</p>
    </div>
    <div class="field"></div>
  </section>

  <section class="piece card-front" aria-label="Business card, name side">
    <div class="band">Dana Whitlock<span>Managing Coordinator</span></div>
    <div class="wordmark"><span class="dot"></span>Trindex</div>
  </section>

  <section class="piece folder" aria-label="Presentation folder">
    <div class="wordmark"><span class="dot"></span>Trindex</div>
  </section>

  <article class="piece letterhead" aria-label="Letterhead">
    <div class="sender">Dana Whitlock<br>Managing Coordinator</div>
    <div class="recipient">To,<br>Jordan Pell<br>Sales Director</div>
    <div class="subject">Updated pricing schedule for compatible parts and supplies</div>
    <div class="body-copy">
      <p>Thank you for your continued partnership with our team. This letter confirms the updated pricing schedule for toner, drums and fuser parts, effective next quarter. Please review the enclosed summary and share any questions with your account manager at your convenience.</p>
      <p>Our compatible product line now includes more than four hundred parts for copiers, printers and multi-function machines, each tested to meet the same output standards as original brand supplies. Orders placed before two in the afternoon ship the same business day from either of our two locations, and dealers across the United States and Latin America can track every shipment online. We also offer volume pricing for service teams that lease and maintain imaging equipment. Should you need samples for evaluation, simply reply to this letter and we will arrange delivery within the week.</p>
    </div>
    <div class="closing">Kind regards,</div>
    <div class="signature" role="img" aria-label="Handwritten signature of Dana Whitlock"></div>
    <footer class="letter-footer">
      <div class="wordmark"><span class="dot"></span>Trindex</div>
      <p>Trindex Supply Corporate Office<br>1820 Harbor Crest Drive<br>Palmera, FL 33400<br>Toll Free: 800-555-0162</p>
      <p>Trindex West Fulfillment Center<br>75 Quarry Lane<br>Silvercreek, NV 89600<br>Phone: 775-555-0190</p>
    </footer>
  </article>

  <section class="piece envelope" aria-label="Number 10 envelope">
    <svg width="266" height="676" viewBox="0 0 266 676" aria-hidden="true">
      <polyline points="0,0 133,130 266,0" fill="none" stroke="var(--rule)" stroke-width="1"/>
    </svg>
    <div class="return">
      <div class="wordmark"><span class="dot"></span>Trindex</div>
      <div>Trindex Supply<br>1820 Harbor Crest Drive<br>Palmera, FL 33400<br>800-555-0162</div>
    </div>
  </section>

</main>
</body>
</html>
```